ROVN branded stationary template

We need associated stationary to accompany our new logo.

The stationary design will be used on business cards, presentation slides and document templates so needs to be provided in an EPS format so that we can adapt it. The design MUST BE ADAPTABLE.

The logo colour is #4a4195 or RGB 85/68/141. Associated colours that can be used in this stationary should compliment this colour. Other colour choices - the preference would be dark and light purples, blues, black and greys. Done how you see fit.

We want the stationary to compliment the overall design of the logo, so clean sharp lines are what we are looking for. It doesn't need to be overly intricate in design - something simple that compliments the look and feel of the logo is what we want. More focused on lines and shapes around the stationary, not any additional logos or pictures.

UK housing providers

Business

Sans Serif

• Clean sharp appearance, nothing overly elaborate.

```html
<!DOCTYPE html>
<html lang="en">
<head>
<meta charset="utf-8">
<title>ROVN Business Card</title>
<link rel="stylesheet" href="https://fonts.googleapis.com/css2?family=Open+Sans:wght@400;600&display=swap">
<style>
  :root {
    --backdrop: #3a3a3a;
    --brand-purple: #675fab;
    --card-white: #ffffff;
    --card-grey: #555454;
    --text-grey: #4a4a4a;
    --text-light: #ffffff;
  }
  * { box-sizing: border-box; margin: 0; padding: 0; }
  html, body {
    width: 1105px; height: 1200px; overflow: hidden;
    background: var(--backdrop);
  }
  .canvas { position: relative; width: 1105px; height: 1200px; }
  .card {
    position: absolute; left: 191px; width: 722px;
    overflow: hidden;
  }
  .card--front { top: 167px; height: 412px; background: var(--card-white); }
  .card--back { top: 623px; height: 410px; background: var(--brand-purple); }

  .brand { position: absolute; display: flex; align-items: center; gap: 18px; }
  .brand__mark { width: 46px; height: 46px; flex: none; }
  .brand__name {
    font-family: "Open Sans", sans-serif; font-weight: 600;
    font-size: 62px; line-height: 1; letter-spacing: 1px;
  }
  .card--front .brand { left: 44px; top: 42px; color: var(--brand-purple); }
  .card--front .brand__mark { background: var(--brand-purple); }
  .card--back .brand { left: 50%; top: 50%; transform: translate(-50%, -62%); color: var(--text-light); }
  .card--back .brand__mark { width: 64px; height: 64px; background: var(--text-light); }
  .card--back .brand__name { font-size: 86px; }

  .holder { position: absolute; right: 32px; top: 56px; text-align: right; font-family: "Open Sans", sans-serif; }
  .holder__name { color: var(--brand-purple); font-weight: 600; font-size: 25px; line-height: 1.2; }
  .holder__title { color: var(--text-grey); font-size: 20px; line-height: 1.3; }
  .holder-accent { position: absolute; right: 0; top: 61px; width: 10px; height: 48px; background: var(--brand-purple); }

  .contact-band {
    position: absolute; left: 0; right: 0; top: 203px; bottom: 0;
    background: var(--card-grey);
  }
  .contact-list {
    position: absolute; left: 26px; top: 20px; list-style: none;
    font-family: "Open Sans", sans-serif; font-size: 19px; color: var(--text-light);
  }
  .contact-list li { display: flex; align-items: center; height: 27.5px; }
  .contact-list svg { width: 18px; height: 18px; margin-right: 10px; fill: var(--brand-purple); }
  .address {
    position: absolute; left: 26px; top: 134px;
    font-family: "Open Sans", sans-serif; font-size: 19px; line-height: 27px; color: var(--text-light);
    font-style: normal;
  }
</style>
</head>
<body>
<main class="canvas">
  <section class="card card--front">
    <div class="brand">
      <span class="brand__mark"></span>
      <span class="brand__name">ROVN</span>
    </div>
    <div class="holder">
      <p class="holder__name">Daniel Hart</p>
      <p class="holder__title">CEO/Founder</p>
    </div>
    <span class="holder-accent"></span>

    <div class="contact-band">
      <ul class="contact-list">
        <li><svg viewBox="0 0 24 24" aria-hidden="true"><path d="M6.6 10.8a15 15 0 0 0 6.6 6.6l2.2-2.2a1 1 0 0 1 1-.25 11.4 11.4 0 0 0 3.6.57 1 1 0 0 1 1 1V20a1 1 0 0 1-1 1A17 17 0 0 1 3 4a1 1 0 0 1 1-1h3.5a1 1 0 0 1 1 1c0 1.250.2 2.45.57 3.57a1 1 0 0 1-.25 1z"/></svg>613 502 8841</li>
        <li><svg viewBox="0 0 24 24" aria-hidden="true"><path d="M7 2h10a1.5 1.5 0 0 1 1.5 1.5v17A1.5 1.5 0 0 1 17 22H7a1.5 1.5 0 0 1-1.5-1.5v-17A1.5 1.5 0 0 1 7 2zm1 3v12h8V5zm4 13.5a1 1 0 1 0 0 2 1 1 0 0 0 0-2z"/></svg>724 391 0586</li>
        <li><svg viewBox="0 0 24 24" aria-hidden="true"><path d="M7 3h10v5H7zM4 9h16a2 2 0 0 1 2 2v6h-4v4H6v-4H2v-6a2 2 0 0 1 2-2zm4 7v3h8v-3z"/></svg>559 270 3318</li>
        <li><svg viewBox="0 0 24 24" aria-hidden="true"><path d="M3 5h18v14H3zm2 2v.5l7 4.5 7-4.5V7z"/></svg>hello@rovnhomes.com</li>
      </ul>
      <address class="address">2140 Linden Row<br>Harrowgate, Westfield 48210</address>
    </div>
  </section>

  <section class="card card--back">
    <div class="brand">
      <span class="brand__mark"></span>
      <span class="brand__name">ROVN</span>
    </div>
  </section>
</main>
</body>
</html>
```